A 1 to 2 page digital flyer, using my existing logo and branding files.

I need a professional1 to 2 page flyer in both digital file and an editable PDF form to advertise service offerings for my coaching and consulting business.
The flyer should be upmarket, professional and conservative in style to meet the expectations of my professional market (doctors, psychologists and executives).
It will be based on my existing logo and brand, see my current website: www.harlowmentoring.com
Here are the key elements needed:
1) First the main product offering (which I should be able to edit myself for future use). In this first case, this features an advertisement for a 'Therapy group for professionals'. (see attached file).
2) The second key text is my bio/profile which includes a photo.
3) The third section is a call to action, including my contact details.
4) The flyer should include my email, website and phone contact details.
5) It should also include some small logos of my professional accrediting organisations.

Target Market(s)

Doctors, psychologists, executives in healthcare.

Industry/Entity Type

Health care and business schools

Font styles to use
Other font styles liked:
• Operetta (headings), Sofia Pro (body text).

Colors
0054AA
0677BA
7BADD7
CADEEF
E8F1F8

Requirements
Must have
• 1. Strong adherence to my brand voice and design elements, as featured on my website and in my branded stationery. 2. Editable text sections in PDF that I can re-use for future advertisements. 3. Suitable size and medium (e.g. A4 size) for sharing digitally via my website, email, and social media. 4) Very prompt design as soon as possible please - quick turnaround will secure the winning place.
Nice to have
• Please use design images and inspiration from my website. An additional stock photo of a therapy group is uploaded as an example
Should not have
• Do not deviate from my brand voice, fonts and colours please.

```html
<!DOCTYPE html>
<html lang="en">
<head>
<meta charset="UTF-8">
<title>Transforming Cultures – Harlow Mentoring</title>
<link href="https://fonts.googleapis.com/css2?family=Playfair+Display:wght@600;700&family=Raleway:wght@300;400;500&display=swap" rel="stylesheet">
<style>
  :root {
    --page-bg: #e3eaf4;
    --navy: #1e3a6e;
    --navy-deep: #17305e;
    --brand-blue: #1b4b96;
    --brand-blue-dark: #163f82;
    --heading-blue: #1a3d86;
    --arc-grey: #a9b0ba;
    --pill-grey: #7c838d;
    --text-dark: #2a3550;
    --white: #ffffff;
  }
  * { margin: 0; padding: 0; box-sizing: border-box; }
  html, body { width: 858px; height: 1200px; overflow: hidden; background: var(--page-bg); }
  .flyer {
    position: relative; width: 858px; height: 1200px; overflow: hidden;
    background: var(--page-bg);
    font-family: "Raleway", Arial, sans-serif; color: var(--text-dark);
  }
  .flyer-shapes { position: absolute; inset: 0; }
  .brand {
    position: absolute; left: 618px; top: 58px; display: flex; align-items: center; gap: 12px;
  }
  .brand-mark { width: 22px; height: 22px; background: var(--brand-blue); }
  .brand-name {
    font-family: "Playfair Display", Georgia, serif; font-weight: 600; color: var(--brand-blue);
    font-size: 26px; line-height: 26px;
  }
  .hero-title {
    position: absolute; left: 68px; top: 168px;
    font-family: "Playfair Display", Georgia, serif; font-weight: 700;
    font-size: 40px; line-height: 52px; color: var(--white); letter-spacing: 1px;
  }
  .hero-tagline {
    position: absolute; left: 68px; top: 298px; width: 360px;
    font-weight: 300; font-size: 24px; line-height: 33px; color: var(--white);
  }
  .profile { position: absolute; left: 60px; top: 624px; width: 400px; }
  .profile-name {
    font-family: "Playfair Display", Georgia, serif; font-weight: 700;
    font-size: 33px; line-height: 38px; color: var(--heading-blue);
  }
  .profile-role { font-size: 12px; color: var(--text-dark); margin-top: 1px; }
  .credentials { position: absolute; left: 60px; top: 752px; width: 420px; }
  .section-heading {
    font-family: "Playfair Display", Georgia, serif; font-weight: 700;
    font-size: 13px; text-transform: uppercase; letter-spacing: .2px;
  }
  .credentials .section-heading { color: var(--text-dark); margin-bottom: 4px; }
  .credential-list { list-style: none; }
  .credential-list li {
    position: relative; padding-left: 16px; font-size: 11.5px; line-height: 18.5px;
  }
  .credential-list li::before {
    content: ""; position: absolute; left: 0; top: 5px; width: 9px; height: 9px;
    border-radius: 50%; background: var(--brand-blue);
  }
  .credential-list li::after {
    content: ""; position: absolute; left: 2.5px; top: 7px; width: 3px; height: 4px;
    border: solid var(--white); border-width: 0 1.3px 1.3px 0; transform: rotate(40deg);
  }
  .approach { position: absolute; left: 530px; top: 613px; width: 300px; color: var(--white); }
  .approach .section-heading { font-size: 15px; margin-bottom: 4px; }
  .approach-text { font-size: 11.5px; line-height: 15.8px; text-align: justify; }
  .approach-points { list-style: none; margin-top: 13px; padding-left: 12px; }
  .approach-points li { font-size: 11.5px; line-height: 15.8px; }
  .approach-points li::before { content: "• "; }
  .accreditation { position: absolute; left: 530px; top: 1036px; }
  .accreditation-label { font-size: 11px; font-weight: 500; color: var(--text-dark); }
  .accreditation-badges { display: flex; align-items: center; gap: 14px; margin-top: 8px; }
  .badge-circle { width: 34px; height: 34px; border-radius: 50%; border: 3px solid #b9a03a; background: #d8dff0; }
  .badge-box { width: 84px; height: 26px; background: #2f3d63; border-radius: 3px; }
  .badge-pill { width: 84px; height: 30px; background: #5a2e8f; border-radius: 3px; }
  .contact-button {
    position: absolute; left: 62px; top: 1061px; width: 130px; height: 28px; border-radius: 14px;
    background: var(--pill-grey); color: var(--white); font-size: 11px; font-weight: 500;
    letter-spacing: .8px; text-transform: uppercase; display: flex; align-items: center; justify-content: center;
  }
  .address { position: absolute; left: 60px; top: 1125px; color: var(--white); font-size: 11.5px; line-height: 16px; }
  .contact-details { position: absolute; left: 342px; top: 1108px; list-style: none; color: var(--white); }
  .contact-details li { display: flex; align-items: center; gap: 7px; font-size: 11.5px; line-height: 16.5px; }
  .contact-details svg { width: 10px; height: 10px; flex: none; }
</style>
</head>
<body>
<main class="flyer">
  <svg class="flyer-shapes" viewBox="0 0 858 1200" width="858" height="1200" aria-hidden="true">
    <defs>
      <linearGradient id="heroTone" x1="0" y1="0" x2="1" y2="1">
        <stop offset="0" stop-color="#3a5485"/>
        <stop offset="1" stop-color="#1f3868"/>
      </linearGradient>
      <linearGradient id="panelTone" x1="0" y1="0" x2="0" y2="1">
        <stop offset="0" stop-color="#173e80"/>
        <stop offset="1" stop-color="#1d4f9c"/>
      </linearGradient>
      <linearGradient id="portraitTone" x1="0" y1="0" x2="0" y2="1">
        <stop offset="0" stop-color="#e9edf3"/>
        <stop offset=".55" stop-color="#c8cfd9"/>
        <stop offset="1" stop-color="#2d4f95"/>
      </linearGradient>
    </defs>

    <!-- grey sweep under hero -->
    <path d="M0 505 C150 560 330 600 470 594 C600 588 680 560 740 505 L740 530 C680 590 600 612 470 612 C330 614 150 580 0 525 Z" fill="var(--arc-grey)"/>

    <!-- hero photo area -->
    <path role="img" aria-label="Photo of a small group meeting in a bright office, tinted navy"
          d="M0 0 H402 C480 60 560 160 595 260 C620 340 640 430 700 505 C620 565 520 585 420 582 C260 576 120 540 0 492 Z"
          fill="url(#heroTone)"/>

    <!-- right blue panel -->
    <path d="M477 583 H560 C690 585 800 520 858 400 V1008 C760 935 680 905 610 905 C540 905 495 940 477 985 Z"
          fill="url(#panelTone)"/>

    <!-- grey ring around portrait -->
    <path d="M700 214 A150 150 0 0 1 805 455" fill="none" stroke="var(--arc-grey)" stroke-width="3"/>
    <circle cx="688" cy="354" r="128" fill="#d3d9e2"/>
    <circle role="img" aria-label="Portrait photo of the consultant in a blue blazer" cx="688" cy="354" r="115" fill="url(#portraitTone)"/>

    <!-- bottom white lobe grey arc -->
    <path d="M455 1010 C490 930 560 900 620 900 C720 900 800 950 858 1000 L858 1015 C790 965 720 925 620 925 C560 925 500 955 475 1040 Z" fill="var(--arc-grey)"/>
    <path d="M450 1020 C470 1100 510 1160 560 1200 H548 C505 1165 470 1110 450 1040 Z" fill="var(--brand-blue-dark)"/>

    <!-- bottom band -->
    <path d="M0 1077 H498 C510 1125 528 1168 548 1200 H0 Z" fill="var(--brand-blue)"/>
  </svg>

  <div class="brand">
    <span class="brand-mark"></span>
    <span class="brand-name">Harlow<br>Mentoring</span>
  </div>

  <h1 class="hero-title">TRANSFORMING<br>CULTURES</h1>
  <p class="hero-tagline">One leader, one team, one organisation at a time.</p>

  <section class="profile">
    <h2 class="profile-name">Daniel Harlow</h2>
    <p class="profile-role">Professor of Organisational Culture &amp; Leadership</p>
  </section>

  <section class="credentials">
    <h3 class="section-heading">Professional credentials:</h3>
    <ul class="credential-list">
      <li>PhD Organisational Leadership and Culture,<br>Kingsgate College (University of Westmere)</li>
      <li>Registered Psychoanalytic Psychotherapist<br>and Group Analyst (MAGA, MNCP)</li>
      <li>Professional Certified Coach<br>(PCC, Global Coaching Alliance)</li>
      <li>Fellow, Institute of Social Anthropology</li>
      <li>Life Member, Ashbury University Anthropological Society</li>
      <li>Fellow, Society of Clinical Medicine</li>
      <li>Fellow, Tertiary Teaching Council</li>
    </ul>
  </section>

  <section class="approach">
    <h3 class="section-heading">How we work</h3>
    <p class="approach-text">Co-design actionable insights. We tailor an approach to fit your specific context. Harness the untapped potential of your informal organisation. We discover and build network-like communities that bridge silos. Enable and mobilise emotional engagement. We help create and sustain the social momentum for meaningful change. Our three-tiered model is designed to catalyse cultural change. It uses key lessons from the world's top business schools to:</p>
    <ul class="approach-points">
      <li>Create positive change in workplace cultures</li>
      <li>Energise the heart of organisations</li>
      <li>Enable values-based leadership</li>
    </ul>
  </section>

  <section class="accreditation">
    <p class="accreditation-label">Accredited by</p>
    <div class="accreditation-badges">
      <span class="badge-circle"></span>
      <span class="badge-box"></span>
      <span class="badge-pill"></span>
    </div>
  </section>

  <div class="contact-button">Contact us</div>

  <p class="address">Suite 310/72 Linden St<br>Fitzroy, Victoria, Australia</p>

  <ul class="contact-details">
    <li><svg viewBox="0 0 10 10"><path d="M2 0.5 L3.6 2.6 L2.7 3.6 C3.3 5 4.9 6.7 6.4 7.3 L7.4 6.4 L9.5 8 L8.4 9.5 C4.5 9.2 0.8 5.5 0.5 1.6 Z" fill="#fff"/></svg>+61 3 9021 5537</li>
    <li><svg viewBox="0 0 10 10"><rect x="0.7" y="1.8" width="8.6" height="6.4" fill="none" stroke="#fff" stroke-width="1"/><path d="M0.9 2.2 L5 5.3 L9.1 2.2" fill="none" stroke="#fff" stroke-width="1"/></svg>info@harlowmentoring.com</li>
    <li><svg viewBox="0 0 10 10"><circle cx="5" cy="5" r="4.3" fill="none" stroke="#fff" stroke-width="1"/><ellipse cx="5" cy="5" rx="1.8" ry="4.3" fill="none" stroke="#fff" stroke-width=".9"/><path d="M0.7 5 H9.3" stroke="#fff" stroke-width=".9"/></svg>www.harlowmentoring.com</li>
  </ul>
</main>
</body>
</html>
```